TV - business card

Tidewell Vantage is an insurance brokerage firm, inovative, proactive, vigorous, which aims to become the leader of the insurance brokers in Anfrica. We should like to get some designs which should be avoided also in Gray / Metallic for the Administration and Orange / Blue for the Managers (ike in the picture sent). The Blue / Green logo is not the correct one, but the source of the file. Please adjust the color accordingly for the business cards. 1 / Orange / Blue 2 / Gray / Metallic We want something classic but which is transmitted strenght, inovation, modernity and most of all, rapidity. We want something start-up like, very punchy and catching eye remaining profesional at the same time. Name: Delton Ashgrove Function: Managing Director Address: N ° 73/74 Cmt. Bolembe - R / C 2B Esquerda - Bairro Quimbuta - Luanda Tel: (+244) 947 385 619 Email: delton.ashgrove@tidewell-v.com Website: www.tidewell-v. com We want classic in the front and creative, colorfull at the back. The cards will be printed in relief, with very high quality of paper.
Industry/Entity Type
Insurance Broker
Colors
Designer to choose colors to be used in the design.
Look and feel

```html
<!DOCTYPE html>
<html lang="en">
<head>
<meta charset="utf-8">
<title>Tidewell Vantage – Business Card</title>
<link rel="stylesheet" href="https://fonts.googleapis.com/css2?family=Roboto:wght@400;500;700;900&display=swap">
<style>
  :root {
    --bg: #e4e4e6;
    --paper: #ffffff;
    --ink-dark: #1f1f20;
    --orange: #f26a21;
    --blue: #2f9bd6;
    --text: #5a5a5a;
    --edge: #f26a21;
  }
  * { box-sizing: border-box; margin: 0; padding: 0; }
  html, body {
    width: 1200px; height: 1200px; overflow: hidden;
    background: var(--bg);
    font-family: "Roboto", Arial, sans-serif;
  }
  .sheet {
    width: 1200px; height: 1200px;
    display: flex; flex-direction: column;
    align-items: center; justify-content: center; gap: 60px;
  }
  .card {
    position: relative;
    width: 900px; height: 514px;
    border-bottom: 6px solid var(--edge);
    border-right: 4px solid var(--edge);
    box-shadow: 0 10px 24px rgba(0,0,0,.18);
  }
  /* Front */
  .card--front { background: var(--paper); }
  .brand {
    position: absolute; display: flex; align-items: center; gap: 12px;
  }
  .card--front .brand { left: 48px; top: 300px; }
  .brand__dot {
    flex: none; border-radius: 50%; border: 5px solid var(--orange);
  }
  .card--front .brand__dot { width: 40px; height: 40px; }
  .brand__name {
    color: var(--orange); font-weight: 900; text-transform: uppercase;
    letter-spacing: .5px; white-space: nowrap;
  }
  .card--front .brand__name { font-size: 26px; }
  .divider {
    position: absolute; left: 392px; top: 120px;
    width: 3px; height: 270px; background: var(--orange);
  }
  .contact { position: absolute; left: 420px; top: 118px; width: 450px; }
  .contact__name { font-size: 30px; font-weight: 700; line-height: 1.1; }
  .contact__first { color: var(--orange); }
  .contact__last { color: var(--blue); }
  .contact__role { font-size: 17px; color: var(--text); margin-top: 4px; }
  .contact__list { list-style: none; margin-top: 34px; font-size: 14px; color: var(--text); line-height: 1.6; }
  .contact__list li + li { margin-top: 10px; }
  .contact__label { color: var(--orange); }
  /* Back */
  .card--back { background: var(--ink-dark); }
  .card--back .brand {
    left: 0; right: 0; top: 0; bottom: 0;
    flex-direction: column; justify-content: center; gap: 28px;
  }
  .card--back .brand__dot { width: 150px; height: 150px; border-width: 10px; }
  .card--back .brand__name { font-size: 62px; }
</style>
</head>
<body>
<main class="sheet">
  <section class="card card--front" aria-label="Card front">
    <div class="brand">
      <span class="brand__dot"></span>
      <span class="brand__name">Tidewell Vantage</span>
    </div>
    <div class="divider"></div>
    <div class="contact">
      <h1 class="contact__name"><span class="contact__first">Delton</span> <span class="contact__last">Ashgrove</span></h1>
      <p class="contact__role">Managing Director</p>
      <ul class="contact__list">
        <li><span class="contact__label">Address:</span> N ° 73/74 Cmt. Bolembe - R / C 2B<br>Esquerda - Bairro Quimbuta - Luanda</li>
        <li><span class="contact__label">Tel:</span> (+244) 947 385 619</li>
        <li><span class="contact__label">Email:</span> delton.ashgrove@tidewell-v.com<br><span class="contact__label">Website:</span> www.tidewell-v. com</li>
      </ul>
    </div>
  </section>
  <section class="card card--back" aria-label="Card back">
    <div class="brand">
      <span class="brand__dot"></span>
      <span class="brand__name">Tidewell Vantage</span>
    </div>
  </section>
</main>
</body>
</html>
```